Brisk Hive 360 Postcard Design, Double-Sided

Please read carefully and see attached. Designers that do not follow these instructions will not be selected. Limit ONE design submission per artist. The ONE design submission shall show both the front and the back designs. Designs must comply with the attached dismensions accounting for the bleed area to prevent designs from being cut off during printing. The attached business card and door tag designs have already been created, printed and are in use. The postcard shall be similar in design to the attached business card and door tag. All of the information that you need is attached. The overall size is 4.12" x 6.12" for the front. The back is different, see attached and scale to match template. I would like the Veteran Owned Business logo added as well. It would also be nice to see my photo incorporated somehow. I like the yellow on the door tag. It helps build contrast and pops out. Again, one design submission per designer that shows both the front and the back.

Target Market(s)

Please read all instructions and see attached.

Industry/Entity Type

Requirements
Must have
• Please read all instructions and see attached.
Nice to have
Should not have

```html
<!DOCTYPE html>
<html lang="en">
<head>
<meta charset="utf-8">
<title>Brisk Hive 360 Postcard</title>
<link href="https://fonts.googleapis.com/css2?family=Poppins:ital,wght@0,500;0,600;0,700;0,800;1,800;1,900&family=Varela+Round&family=Arimo&display=swap" rel="stylesheet">
<style>
:root{
  --stage:#a6a7ab;
  --ink:#0b0b0b;
  --yellow:#f7ec13;
  --white:#ffffff;
  --red:#e5141d;
  --navy:#1f2f6b;
  --photo-wood:#8a7356;
  --photo-steel:#b9c1c9;
  --photo-tools:#7b5a3a;
  --photo-tech:#1b5d9a;
}
*{margin:0;padding:0;box-sizing:border-box}
html,body{width:898px;height:1200px;overflow:hidden;background:var(--stage)}
.canvas{position:relative;width:898px;height:1200px;background:var(--stage)}
.card{position:absolute;left:88px;width:722px;overflow:hidden;box-shadow:4px 6px 10px rgba(0,0,0,.35)}
.card-front{top:88px;height:486px;background:var(--ink)}
.card-back{top:626px;height:485px;background:var(--white)}
.layer{position:absolute;left:0;top:0}
.abs{position:absolute;line-height:1;white-space:nowrap}
.heading{font-family:"Poppins",sans-serif}
.body{font-family:"Varela Round",sans-serif}
.website{font-family:"Poppins",sans-serif;font-weight:600;font-size:24px;color:var(--yellow)}
.owner-name{left:31px;top:62px;font-family:"Poppins",sans-serif;font-weight:700;font-size:18px;color:var(--white)}
.owner-role{left:31px;top:80px;font-family:"Poppins",sans-serif;font-weight:500;font-size:12px;color:var(--white)}
.inquire{left:218px;top:207px;font-family:"Poppins",sans-serif;font-weight:700;color:var(--ink)}
.inquire .accent{color:var(--red);font-size:35px}
.inquire .rest{font-size:25px}
.contact{left:245px;font-family:"Varela Round",sans-serif;font-size:18px;color:var(--ink)}
.contact-icon{position:absolute;left:219px}
.section-title{font-family:"Poppins",sans-serif;font-weight:700;font-size:22px;color:var(--white)}
.section-sub{font-family:"Varela Round",sans-serif;font-size:9.5px;color:var(--white)}
.list{list-style:none;position:absolute;font-family:"Varela Round",sans-serif;color:var(--white)}
.list li::before{content:"• "}
.benefits{left:144px;top:395px;font-size:13px;line-height:16px}
.services{left:298px;top:378px;font-size:10.5px;line-height:12.7px}
.divider{position:absolute;left:280px;top:360px;width:1.5px;height:104px;background:var(--white)}
.brand-seal{position:absolute;border-radius:50%;display:flex;align-items:center;justify-content:center;text-align:center;font-family:"Poppins",sans-serif;font-weight:800;line-height:1.1}
.seal-small{left:29px;top:361px;width:96px;height:96px;background:var(--white);color:var(--ink);font-size:13px}
.seal-large{left:92px;top:135px;width:212px;height:212px;background:var(--ink);color:var(--white);font-size:26px}
.partner-badge{position:absolute;border-radius:50%;background:var(--navy);border:4px solid var(--red)}
.postage{position:absolute;left:582px;top:20px;width:117px;height:117px;border:1px solid #8d8d8d;display:flex;align-items:center;justify-content:center;font-family:"Poppins",sans-serif;font-weight:800;font-size:12px;color:var(--ink);padding-bottom:38px}
.address{position:absolute;left:441px;top:276px;font-family:"Arimo",sans-serif;font-size:16px;line-height:23px;color:#222}
</style>
</head>
<body>
<div class="canvas">

  <!-- FRONT -->
  <section class="card card-front">
    <svg class="layer" width="722" height="486" viewBox="0 0 722 486">
      <defs>
        <clipPath id="photo-column"><polygon points="428,0 722,0 722,486 428,486 520,242"/></clipPath>
        <linearGradient id="g-hooks" x1="0" y1="0" x2="1" y2="1"><stop offset="0" stop-color="#dfe5ec"/><stop offset="1" stop-color="#c2c9cf"/></linearGradient>
        <linearGradient id="g-tools" x1="0" y1="0" x2="1" y2="1"><stop offset="0" stop-color="#6d5a48"/><stop offset=".6" stop-color="#a8743f"/><stop offset="1" stop-color="#3a8a92"/></linearGradient>
        <radialGradient id="g-tech" cx=".5" cy=".5" r=".7"><stop offset="0" stop-color="#4fb7e6"/><stop offset="1" stop-color="#0c3a78"/></radialGradient>
        <linearGradient id="g-person" x1="0" y1="0" x2="0" y2="1"><stop offset="0" stop-color="#e6e6e8"/><stop offset="1" stop-color="#c9cbd0"/></linearGradient>
      </defs>
      <polygon class="info-band" points="0,192 481,192 500,242 463,341 0,341" fill="var(--white)"/>
      <polygon class="chevron-stripe" points="408,0 419,0 511,242 419,486 408,486 500,242" fill="var(--yellow)"/>
      <g clip-path="url(#photo-column)">
        <rect x="420" y="0" width="302" height="162" fill="url(#g-hooks)" role="img" aria-label="Photo of picture hanging hooks and brass nails"/>
        <rect x="420" y="162" width="302" height="162" fill="url(#g-tools)" role="img" aria-label="Photo of a tool belt with hand tools and a cordless drill"/>
        <rect x="420" y="324" width="302" height="162" fill="url(#g-tech)" role="img" aria-label="Illustration of a wireless router and devices on a digital grid"/>
      </g>
      <rect x="0" y="192" width="164" height="149" fill="url(#g-person)" role="img" aria-label="Portrait photo of the owner"/>
      <rect x="35" y="145" width="376" height="2.5" fill="var(--yellow)"/>
      <text x="31" y="134" textLength="378" lengthAdjust="spacingAndGlyphs" font-family="Poppins, sans-serif" font-style="italic" font-weight="900" font-size="50" fill="var(--yellow)">BRISK HIVE 360</text>
      <text x="222" y="177" text-anchor="middle" font-family="Poppins, sans-serif" font-style="italic" font-weight="900" font-size="30" fill="var(--yellow)">HANDYMAN</text>
    </svg>

    <svg class="abs" style="left:30px;top:25px" width="28" height="28" viewBox="0 0 28 28" fill="none" stroke="var(--yellow)" stroke-width="1.6">
      <circle cx="14" cy="14" r="11"/><ellipse cx="14" cy="14" rx="5" ry="11"/><line x1="3" y1="14" x2="25" y2="14"/><line x1="5" y1="8" x2="23" y2="8"/><line x1="5" y1="20" x2="23" y2="20"/>
    </svg>
    <div class="abs website" style="left:71px;top:26px">Briskhive360.com</div>
    <div class="abs owner-name">DORIAN K. WALSH</div>
    <div class="abs owner-role">OWNER &amp; HANDYMAN</div>

    <div class="partner-badge" style="left:125px;top:227px;width:80px;height:80px" role="img" aria-label="Veteran owned business badge"></div>

    <div class="abs inquire"><span class="accent">TEXT</span> <span class="rest">TO INQUIRE</span></div>

    <svg class="contact-icon" style="top:247px" width="18" height="18" viewBox="0 0 24 24" fill="none" stroke="var(--ink)" stroke-width="1.8"><path d="M5 3h4l2 5-2.5 1.5a11 11 0 0 0 6 6L16 13l5 2v4a2 2 0 0 1-2 2A17 17 0 0 1 3 5a2 2 0 0 1 2-2z"/></svg>
    <div class="abs contact" style="top:247px">(555) 014-2287</div>
    <svg class="contact-icon" style="top:276px" width="18" height="18" viewBox="0 0 24 24" fill="none" stroke="var(--ink)" stroke-width="1.8"><path d="M12 22s7-7 7-12a7 7 0 0 0-14 0c0 5 7 12 7 12z"/><circle cx="12" cy="10" r="2.5"/></svg>
    <div class="abs contact" style="top:276px">Harbor Point, Florida</div>
    <svg class="contact-icon" style="top:304px" width="18" height="18" viewBox="0 0 24 24" fill="none" stroke="var(--ink)" stroke-width="1.8"><path d="M22 2L11 13"/><path d="M22 2l-7 20-4-9-9-4z"/></svg>
    <div class="abs contact" style="top:304px">Service@BriskHive360.com</div>

    <div class="brand-seal seal-small">Brisk<br>Hive 360</div>

    <div class="abs section-title" style="left:144px;top:361px">BENEFITS</div>
    <div class="abs section-sub" style="left:145px;top:380px">OF USING OUR SERVICES</div>
    <ul class="list benefits">
      <li>Fast Response</li><li>High Quality</li><li>Fair Pricing</li><li>Veteran Owned</li>
    </ul>
    <div class="divider"></div>
    <div class="abs section-title" style="left:298px;top:361px">SERVICES:</div>
    <ul class="list services">
      <li>Assembly</li><li>Small Repairs</li><li>Wifi / Router Setup</li><li>Fabrication</li><li>Hanging Items</li><li>Wireless Device Setup</li><li>Odd Jobs</li>
    </ul>
  </section>

  <!-- BACK -->
  <section class="card card-back">
    <svg class="layer" width="722" height="485" viewBox="0 0 722 485">
      <rect x="0" y="0" width="240" height="245" fill="#6e6253" role="img" aria-label="Photo of furniture being assembled"/>
      <rect x="240" y="0" width="330" height="245" fill="#4d5660" role="img" aria-label="Photo of assembly instructions, dowels and a clamp"/>
      <rect x="0" y="245" width="240" height="240" fill="#57524e" role="img" aria-label="Photo of hands installing window blinds"/>
      <rect x="240" y="245" width="330" height="240" fill="#3e4650" role="img" aria-label="Photo of hands fixing a cabinet"/>
      <polygon class="step-yellow" points="561,0 722,0 722,485 129,485 129,380 379,380 379,119 561,119" fill="var(--yellow)"/>
      <polygon class="step-black" points="565,0 722,0 722,485 133,485 133,384 383,384 383,123 565,123" fill="var(--ink)"/>
      <polygon class="step-white" points="579,0 722,0 722,485 146,485 146,396 398,396 398,136 579,136" fill="var(--white)"/>
    </svg>

    <svg class="abs" style="left:30px;top:24px" width="28" height="28" viewBox="0 0 28 28" fill="none" stroke="var(--yellow)" stroke-width="1.6">
      <circle cx="14" cy="14" r="11"/><ellipse cx="14" cy="14" rx="5" ry="11"/><line x1="3" y1="14" x2="25" y2="14"/><line x1="5" y1="8" x2="23" y2="8"/><line x1="5" y1="20" x2="23" y2="20"/>
    </svg>
    <div class="abs website" style="left:71px;top:25px">Briskhive360.com</div>

    <div class="partner-badge" style="left:457px;top:20px;width:80px;height:80px" role="img" aria-label="Veteran owned business badge"></div>

    <div class="brand-seal seal-large">Brisk<br>Hive 360</div>

    <div class="postage">POSTAGE</div>

    <div class="address">John Smith<br>123 Main Street<br>Small Town, USA 00000-0000</div>
  </section>

</div>
</body>
</html>
```